Business card for a boutique travel agency VELARIEN

we need a business card design - double sided. We would like to have a very elegant, sophisticated but modern design. we are travel consultants and our business focus is Europe, mainly the city of Paris. We would like to receive designs in white and silver, black color but if you are confident that we should pick up a color to make it different and more beautful...go ahead! We are going to give business cards to our clients and business partners. It is important to be perceived as elegant, modern and trustful. Please check jpg references.

Target Market(s)

Velarien primary clients are individuals, couples and affinity groups of high-net-worth who travel for leisure at least once per year. Seeking the ultimate travel experience, the target clients demand the finest quality activities and accommodations accompanied by a superior level of service.

Industry/Entity Type

Travel Industry

Contact Information for Business Card

Lucinda Farrow
- lucinda@velarien-example.com
- +55 11 98347.2516
- velarien-example.com
- unique travel experiences (we would like to see this signature printed as a detail)

Font styles to use
Sans Serif

Colors

Designer to choose colors to be used in the design.

Requirements
Must have
• the Velarien logo that I have attached
Nice to have
• we would like to have some nice detail, something different that shows that we care about,... we are detail oriented.
Should not have
• decorative fonts

```html
<!DOCTYPE html>
<html lang="en">
<head>
<meta charset="utf-8">
<title>Velarien – Business Card</title>
<link href="https://fonts.googleapis.com/css2?family=Josefin+Sans:wght@300;400&display=swap" rel="stylesheet">
<style>
  :root {
    --backdrop: #ececec;
    --card: #4a4a4b;
    --card-light: #525253;
    --card-dark: #424243;
    --wordmark-tone: #3a3a3b;
    --ink: #e4e4e4;
    --ink-soft: #bdbdbd;
  }
  * { margin: 0; padding: 0; box-sizing: border-box; }
  html, body {
    width: 1200px;
    height: 787px;
    overflow: hidden;
    background: var(--backdrop);
    font-family: "Josefin Sans", sans-serif;
  }
  .canvas {
    position: relative;
    width: 1200px;
    height: 787px;
    display: flex;
    align-items: center;
    justify-content: center;
    gap: 60px;
  }
  .card {
    position: relative;
    width: 500px;
    height: 286px;
    background: linear-gradient(135deg, var(--card-light) 0%, var(--card) 45%, var(--card-dark) 100%);
    box-shadow: 0 18px 30px rgba(0,0,0,0.16), 0 2px 5px rgba(0,0,0,0.12);
    overflow: hidden;
  }
  /* Front side: oversized tone-on-tone wordmark */
  .card-front .wordmark {
    position: absolute;
    top: 50%;
    left: 50%;
    transform: translate(-50%, -46%);
    white-space: nowrap;
    font-weight: 300;
    font-size: 84px;
    letter-spacing: 0.14em;
    color: var(--wordmark-tone);
  }
  /* Back side: contact block */
  .card-back .contact {
    position: absolute;
    left: 62px;
    bottom: 34px;
    color: var(--ink);
    font-weight: 300;
    text-transform: uppercase;
  }
  .contact .name {
    font-size: 20px;
    font-weight: 400;
    letter-spacing: 0.02em;
    line-height: 1;
  }
  .contact .position {
    font-size: 10px;
    letter-spacing: 0.08em;
    color: var(--ink-soft);
    margin-top: 3px;
  }
  .contact .address {
    font-size: 10px;
    letter-spacing: 0.08em;
    color: var(--ink-soft);
    margin: 18px 0 0 22px;
  }
  .contact .details {
    list-style: none;
    margin: 18px 0 0 38px;
    font-size: 11px;
    letter-spacing: 0.05em;
    line-height: 1.45;
  }
  .details .social {
    display: inline-flex;
    align-items: center;
    gap: 4px;
    margin-right: 10px;
  }
  .details .social::before {
    content: "";
    width: 8px;
    height: 8px;
    background: var(--ink);
    display: inline-block;
    margin-top: -2px;
  }
</style>
</head>
<body>
  <main class="canvas">
    <section class="card card-front" aria-label="Card front">
      <div class="wordmark">VELARIEN</div>
    </section>

    <section class="card card-back" aria-label="Card back">
      <div class="contact">
        <p class="name">Name Name</p>
        <p class="position">Position</p>
        <p class="address">Adress</p>
        <ul class="details">
          <li>velarien-example.com</li>
          <li><span class="social">Velarien</span><span class="social">Velarien</span></li>
          <li>name@velarien-example.com</li>
        </ul>
      </div>
    </section>
  </main>
</body>
</html>
```